BrindleStaffing Business Card Design

We are a staffing company finding positions for dedicated nurses and physicians.

Target Market(s)

Business Professionals

Industry/Entity Type

Staffing

Contact Information for Business Card

Gregory Malden
Chairman
417 39th Crescent South
SAINT PETERSBURG FL 33719
813-555-0147 Mobile
813-555-0183 Fax
gmalden@brindlestaffing.example
www.brindlestaffing.example

Font styles to use
Sans Serif

Colors
fbee3e
f04a50
f37122

Requirements
Must have
• Logo Attached, see colors below. We'd like to see Yellow, Orange and Red.

```html
<!DOCTYPE html>
<html lang="en">
<head>
<meta charset="utf-8">
<title>BrindleStaffing Business Card</title>
<link href="https://fonts.googleapis.com/css2?family=Poppins:wght@600&family=Questrial&display=swap" rel="stylesheet">
<style>
  :root {
    --backdrop: #d9d9d9;
    --card: #e6e6e6;
    --yellow: #fbee3e;
    --red: #f04a50;
    --orange: #f37122;
    --text: #5f5f5f;
  }
  * { margin: 0; padding: 0; box-sizing: border-box; }
  html, body {
    width: 1200px; height: 1200px; overflow: hidden;
    background: var(--backdrop);
  }
  .sheet { position: relative; width: 1200px; height: 1200px; }
  .card {
    position: absolute; left: 227px; width: 745px; height: 425px;
    background: var(--card);
  }
  .card--front { top: 135px; }
  .card--back { top: 638px; display: flex; align-items: center; justify-content: center; }

  .brand {
    display: flex; align-items: center; gap: 14px;
    font-family: "Poppins", sans-serif; font-weight: 600;
    font-size: 66px; letter-spacing: -1px; color: var(--orange); line-height: 1;
  }
  .brand__dot { width: 22px; height: 22px; border-radius: 50%; background: var(--red); }
  .card--front .brand { position: absolute; left: 36px; top: 58px; }

  .person { position: absolute; left: 36px; top: 222px; }
  .person__name {
    font-family: "Poppins", sans-serif; font-weight: 600; font-size: 22px; line-height: 1;
  }
  .person__first { color: var(--orange); }
  .person__last { color: var(--red); }
  .person__role {
    font-family: "Questrial", sans-serif; font-size: 17px; color: var(--text); margin-top: 6px;
  }
  .rule { position: absolute; left: 36px; top: 289px; width: 64px; height: 4px; background: var(--yellow); }

  .contact {
    position: absolute; left: 35px; top: 314px;
    font-family: "Questrial", sans-serif; font-size: 17px; color: var(--text); line-height: 22px;
  }
  .contact__address { margin-bottom: 13px; }
  .contact__label { color: var(--orange); }
  .contact__sep { color: var(--red); }
</style>
</head>
<body>
<div class="sheet">
  <section class="card card--front">
    <div class="brand"><span>BrindleStaffing</span><span class="brand__dot"></span></div>
    <div class="person">
      <p class="person__name"><span class="person__first">Gregory</span> <span class="person__last">Malden</span></p>
      <p class="person__role">Chairman</p>
    </div>
    <div class="rule"></div>
    <div class="contact">
      <p class="contact__address">417 39th Crescent South SAINT PETERSBURG FL 33719</p>
      <p><span class="contact__label">P :</span> 813-555-0147 <span class="contact__sep">/</span> <span class="contact__label">F :</span> 813-555-0183</p>
      <p>gmalden@brindlestaffing.example <span class="contact__sep">/</span> www.brindlestaffing.example</p>
    </div>
  </section>
  <section class="card card--back">
    <div class="brand"><span>BrindleStaffing</span><span class="brand__dot"></span></div>
  </section>
</div>
</body>
</html>
```